IT Company Business Card Design w/Stationary Design

We have a great logo we like! We are looking to redesign our business cards and all company logo'd merchandise/materials.

We are an IT Company located near the Bay Area (San Francisco, CA). We specialize in Managed Services and offer complete IT Computer and Network Support to Businesses of all sizes. We thrive on making a lasting impression. We have been doing IT for 15yrs+ but are young at heart. We like to stand out and be different. We want to be unique and have a recognizable brand. We need our logo to represent who we are. We are young, professional, creative and outstanding. We don't want to blend in, we want to stand out. Our business card needs to stand out and grab attention. Something Bold, yet simple and clean. (I will provide ideas of what we like to give a taste of what we are looking for).

The design can include any kind of texture/artistic design or sizing EXCEPT please "no square card designs" as they don't seem to fit in wallets very well. We dont mind curved edges, rounded corners, vertical layouts or horizontal layouts, embossing, letter press or raised surfaces. Again, we dont want to look average or plain or boring. :) Be creative - yet practical! We have ordered from ZEPL designs before and been very happy. Their card sizes tend to be a little different, so beware. Hope this helps!

Target Market(s)

Businesses - Small to Medium, Corporations, Publicly Traded Companies

Industry/Entity Type

Business

Contact Information for Business Card

Harbor Circuit IT
7180 Dorrance Avenue
Suite K
Modesto, CA 95419

Office 209.555.0137
Direct 209.555.0162
Cell 209.555.0188

Gary Stroud
Founder, CEO
www.hcxit.example
gstroud@hcxit.example

Locations Serviced: Modesto, Stockton, Pleasanton, Fresno (incorporate this on the card ONLY if there's a good place to do so).

What we specialize in: Computer, Network, Voice, Data. (IT Services)

Our Logo Colors: Black and Blue (#006699). Open to using grey or orange as well - but not required. Don't want too busy....

Logo Font: "Voralyn" (Will attach logo font). We want type style to be clean. You can show different font types including our logo font - and we are open to other font ideas.

The logo can be separated. You can use elements together or apart. Surprise us! :) We "REALLY" want the "hc" to be our identifier/our brand people recognize.

Font styles to use
Sans Serif

Colors
0355a3
3176b5
f37122
f78f20
faa54b
474747
aaaaaa
757575
000000

Requirements
Must have
• Bold, Big, Colorful, Modern/yet Fun, Clean Design, Stand Out Presence, Texture would be welcomed - but not necessary, Card design shape can include cut corners or rounded or square edges. Be creative. (HOWEVER, we don't want a square design because we have found it doesn't fit in wallets that easily).
• We do like using ZEPL printing company (Which they have particular sizing on their card templates - beware), but are open to other design templates/printing companies as well. We just want to make sure its easy to find a print company to do our work. Too unique could be costly and hard to get cards printed.
• Colors to use: Our logo Blue (#006699), with either whites, grays, black, shades of our blue, and maybe a pinch of orange if needed. Primarily, blue, white, gray or black.
Nice to have
• Texture would be cool or little different edging or shape - but nothing too costly to print. I have seen cards with 3 sharp edges and one round edge. Something like that would be cool as an option. Or a vertical card.
• I love a faded watermark look. It would be nice to see some shading of our circle logo on a few designs. The circle with "hc" in it OR.... taking just the "hc" and using it alone.
Should not have
• No square card designs. Nothing too expensive or elaborate to print. No busy fonts. Do not like Times New Roman type fonts (too old looking). Not a lot of orange (if you even choose to use some orange).

```html
<!DOCTYPE html>
<html lang="en">
<head>
<meta charset="utf-8">
<title>Harbor Circuit IT – Business Card</title>
<link rel="stylesheet" href="https://fonts.googleapis.com/css2?family=Lato:wght@400;700;900&display=swap">
<style>
  :root {
    --brand-blue: #1a9fd0;
    --brand-blue-deep: #0a78b0;
    --brand-blue-light: #3ab6e2;
    --card-white: #ffffff;
    --card-grey: #eef0f1;
    --text-grey: #4a4a4a;
    --text-soft: #8a8a8a;
    --page-bg: #e6e3de;
  }
  * { box-sizing: border-box; margin: 0; padding: 0; }
  html, body {
    width: 1200px; height: 1023px; overflow: hidden;
    background: var(--page-bg);
    font-family: "Lato", sans-serif;
  }
  .stage { position: relative; width: 1200px; height: 1023px; }
  .card {
    position: absolute; width: 700px; height: 400px;
    border-radius: 28px; overflow: hidden;
    box-shadow: 0 10px 30px rgba(0,0,0,.18);
  }
  /* Front */
  .card--front {
    left: 80px; top: 70px;
    background: linear-gradient(135deg, var(--card-white) 55%, var(--card-grey));
  }
  .front__band {
    position: absolute; right: 0; top: 0; width: 60px; height: 100%;
    background: linear-gradient(180deg, var(--brand-blue-light), var(--brand-blue-deep));
  }
  .front__circle {
    position: absolute; right: 40px; top: 50px;
    width: 300px; height: 300px; border-radius: 50%;
    background: radial-gradient(circle at 40% 35%, var(--brand-blue-light), var(--brand-blue-deep));
    box-shadow: 0 0 0 14px var(--card-white), 0 0 0 17px rgba(26,159,208,.25);
    display: flex; align-items: center; justify-content: center;
  }
  .front__brand {
    color: var(--card-white); font-weight: 900; font-size: 34px;
    text-align: center; line-height: 1.1; letter-spacing: .5px;
  }
  .front__info {
    position: absolute; left: 44px; top: 44px; width: 300px;
    color: var(--text-grey); font-size: 17px; line-height: 1.4;
  }
  .person__name { color: var(--brand-blue); font-weight: 900; font-size: 22px; }
  .person__title { color: var(--text-soft); font-size: 16px; margin-bottom: 14px; }
  .address { margin-bottom: 14px; }
  .contact-list { list-style: none; margin-bottom: 16px; }
  .contact-list li { display: flex; align-items: center; gap: 8px; }
  .contact-list svg { width: 16px; height: 16px; flex: none; }
  .locations__label { color: var(--brand-blue); font-weight: 700; }
  /* Back */
  .card--back {
    left: 420px; top: 540px;
    background: linear-gradient(160deg, var(--brand-blue-light), var(--brand-blue-deep));
  }
  .back__texture {
    position: absolute; inset: 0;
    background: radial-gradient(circle at 30% 30%, rgba(255,255,255,.12), rgba(255,255,255,0) 70%);
  }
  .back__brand {
    position: absolute; left: 0; right: 0; top: 140px;
    display: flex; align-items: center; justify-content: center; gap: 18px;
  }
  .back__dot { width: 80px; height: 80px; border-radius: 50%; background: var(--card-white); }
  .back__name { color: var(--card-white); font-weight: 900; font-size: 46px; letter-spacing: 1px; }
  .back__web {
    position: absolute; left: 40px; bottom: 34px;
    color: var(--card-white); font-size: 17px; letter-spacing: 1px;
  }
</style>
</head>
<body>
<main class="stage">
  <section class="card card--front">
    <div class="front__band"></div>
    <div class="front__circle">
      <span class="front__brand">Harbor<br>Circuit IT</span>
    </div>
    <div class="front__info">
      <p class="person__name">Gary Stroud</p>
      <p class="person__title">Founder, CEO</p>
      <p class="address">7180 Dorrance Avenue Suite K<br>Modesto, CA 95419</p>
      <ul class="contact-list">
        <li><svg viewBox="0 0 16 16"><path d="M3 2h3l1 3-2 1.5a8 8 0 0 0 4.5 4.5L11 9l3 1v3a1 1 0 0 1-1 1A11 11 0 0 1 2 3a1 1 0 0 1 1-1z" fill="#1a9fd0"/></svg>209.555.0188</li>
        <li><svg viewBox="0 0 16 16"><rect x="2" y="3" width="12" height="10" rx="1.5" fill="none" stroke="#1a9fd0" stroke-width="1.6"/></svg>209.555.0137 (Office)</li>
        <li><svg viewBox="0 0 16 16"><rect x="2" y="3" width="12" height="10" rx="1.5" fill="none" stroke="#1a9fd0" stroke-width="1.6"/></svg>209.555.0162 (Direct)</li>
        <li><svg viewBox="0 0 16 16"><rect x="1.5" y="3" width="13" height="10" rx="1" fill="#1a9fd0"/><path d="M2 4l6 5 6-5" fill="none" stroke="#fff" stroke-width="1.3"/></svg>gstroud@hcxit.example</li>
      </ul>
      <p class="locations__label">Locations Serviced:</p>
      <p class="locations__list">Ridgevale, Larkmoor,<br>Pinecrest, Dunhollow.</p>
    </div>
  </section>

  <section class="card card--back">
    <div class="back__texture" role="img" aria-label="Faint repeating brand pattern in lighter blue tones"></div>
    <div class="back__brand">
      <span class="back__dot"></span>
      <span class="back__name">Harbor Circuit IT</span>
    </div>
    <p class="back__web">www.hcxit.example</p>
  </section>
</main>
</body>
</html>
```